E-mail Ad Design Project

I would like a lower banner ad designed for placement within an e-mail. The size has to be 450px x 230px (6in x 3.07in) and must be either a GIF or JPEG, not to exceed 30K.

We are a medical billing company that provides services to physical therapy practices in Florida, and this ad is intended for owners and office managers of physical therapy businesses. We provide therapy offices with practice management software, submit medical claims on behalf of their patients, follow-up with insurance companies on outstanding claims, and also perform necessary back-end collections with patient balances. We also are able to interface with popular therapy documentation products to streamline data entry.

The design colors should incorporate our logo and red/blue colors (see www.clinicianharbor.net).

Target Market(s)

Physical therapists and administrators of physical therapy offices

Industry/Entity Type

Physical Therapy

Requirements
Must have
• Grabbing/heading text:

Tired of Denials and Confusing Rejection Codes?
We Take the Pain Out of Medical Billing.

Offer:

Get Started Today with 2 Free Months of Billing
Nice to have
• We provide services mainly to Florida therapists, so it would be nice to have an image or text that highlights this fact. Also, the e-mail campaign this is a part of will be sent to Florida recipients.

```html
<!DOCTYPE html>
<html lang="en">
<head>
<meta charset="utf-8">
<title>Clinician Harbor – Medical Billing Banner</title>
<link rel="stylesheet" href="https://fonts.googleapis.com/css2?family=Arimo:wght@400;700&display=swap">
<style>
  :root {
    --navy: #1c2b4f;
    --banner-blue: #1a63c4;
    --banner-blue-dark: #0c3a8a;
    --accent-red: #d3201e;
    --accent-red-dark: #a51311;
    --button-top: #2f7fe0;
    --button-bottom: #0b3f9a;
    --white: #ffffff;
    --photo-light: #eef2f6;
    --photo-mid: #c9d3de;
    --photo-warm: #d9c2ae;
  }
  html, body {
    margin: 0;
    padding: 0;
    overflow: hidden;
    background: var(--white);
  }
  .ad {
    position: relative;
    width: 1200px;
    height: 613px;
    overflow: hidden;
    background: var(--white);
    font-family: "Arimo", Arial, sans-serif;
  }
  .ad__photo {
    position: absolute;
    left: 0;
    top: 250px;
    width: 1200px;
    height: 363px;
    background:
      radial-gradient(ellipse 260px 300px at 150px 200px, var(--photo-warm) 0%, rgba(217,194,174,0) 100%),
      linear-gradient(180deg, var(--photo-light) 0%, var(--photo-mid) 100%);
  }
  .ad__heading {
    position: absolute;
    top: 4px;
    left: 0;
    width: 1200px;
    margin: 0;
    text-align: center;
    color: var(--navy);
    font-weight: 700;
    font-size: 64px;
    line-height: 68px;
    letter-spacing: -0.5px;
  }
  .ad__graphics {
    position: absolute;
    left: 0;
    top: 0;
  }
  .ad__logo {
    position: absolute;
    left: 0;
    top: 507px;
    width: 427px;
    height: 74px;
    background: var(--white);
    display: flex;
    align-items: center;
    justify-content: center;
    color: var(--navy);
    font-weight: 700;
    font-size: 34px;
    letter-spacing: 0.5px;
    white-space: nowrap;
  }
  .ad__cta {
    position: absolute;
    left: 733px;
    top: 459px;
    width: 432px;
    height: 106px;
    border-radius: 10px;
    background: linear-gradient(180deg, var(--button-top) 0%, var(--button-bottom) 100%);
    border: 3px solid var(--white);
    box-sizing: border-box;
    display: flex;
    align-items: center;
    justify-content: center;
    color: var(--white);
    font-weight: 700;
    font-size: 38px;
    white-space: nowrap;
    text-decoration: none;
  }
</style>
</head>
<body>
<div class="ad">
  <div class="ad__photo" role="img" aria-label="Photo of a smiling physician in a white coat in the foreground, with office staff and a patient at a front desk behind her"></div>

  <h1 class="ad__heading">Tired of Denials &amp; Confusing<br>Rejection Codes?</h1>

  <svg class="ad__graphics" width="1200" height="613" viewBox="0 0 1200 613">
    <defs>
      <linearGradient id="bannerFill" x1="0" y1="0" x2="0" y2="1">
        <stop offset="0" stop-color="#1a63c4"/>
        <stop offset="1" stop-color="#0c3a8a"/>
      </linearGradient>
    </defs>
    <path d="M107 205 Q611 145 1115 205 L1115 268 Q611 318 107 268 Z" fill="var(--accent-red)"/>
    <path d="M107 192 Q611 135 1115 192 L1115 254 Q611 302 107 254 Z" fill="url(#bannerFill)" stroke="var(--white)" stroke-width="3"/>
    <text x="611" y="212" text-anchor="middle" fill="var(--white)" font-family="Arimo, Arial, sans-serif" font-weight="700" font-size="42">WE TAKE THE PAIN OUT</text>
    <text x="611" y="260" text-anchor="middle" fill="var(--white)" font-family="Arimo, Arial, sans-serif" font-weight="700" font-size="42">OF MEDICAL BILLING</text>

    <g transform="translate(968 375)">
      <g fill="var(--accent-red)">
        <rect x="-86" y="-86" width="172" height="172"/>
        <rect x="-86" y="-86" width="172" height="172" transform="rotate(22.5)"/>
        <rect x="-86" y="-86" width="172" height="172" transform="rotate(45)"/>
        <rect x="-86" y="-86" width="172" height="172" transform="rotate(67.5)"/>
      </g>
      <circle r="88" fill="none" stroke="var(--accent-red-dark)" stroke-width="2"/>
      <text y="-12" text-anchor="middle" fill="var(--white)" font-family="Arimo, Arial, sans-serif" font-weight="700" font-size="76">2</text>
      <text y="24" text-anchor="middle" fill="var(--white)" font-family="Arimo, Arial, sans-serif" font-weight="700" font-size="27">free Months</text>
      <text y="58" text-anchor="middle" fill="var(--white)" font-family="Arimo, Arial, sans-serif" font-weight="700" font-size="27">of Billing</text>
    </g>
  </svg>

  <div class="ad__logo">CLINICIAN HARBOR</div>

  <a class="ad__cta" href="#">Get Started NOW</a>
</div>
</body>
</html>
```